Solar Advertising Flier to generate Biz

I need a advertisement that generates business to be used in a mailer for marketing purposes.

Im attaching a file that is a an idea of advertisement.
I do not want the "ZVN" specific information on it.
I want the background solar panels.
Same information as the ad.
And I've attached my Logo - I want the color scheme to match this.

Thank you

Target Market(s)

Middle to Upper Class Home Owners

Industry/Entity Type

Solar Energy

Requirements
Must have
• A call to action
• A professional look
Nice to have
• A family
• Great looking solar panels
Should not have
• Cartoons

```html
<!DOCTYPE html>
<html lang="en">
<head>
<meta charset="utf-8">
<title>Go Solar – Brightfield Energy</title>
<link href="https://fonts.googleapis.com/css2?family=Open+Sans:ital,wght@0,400;0,600;0,700;0,800;1,700&family=Arimo:wght@400;700&display=swap" rel="stylesheet">
<style>
  :root{
    --blue:#1189d0;
    --blue-dark:#0b6fb0;
    --green:#8dc63f;
    --green-light:#b5de6a;
    --orange:#f07b22;
    --orange-dark:#e0651a;
    --ink:#222;
    --white:#fff;
    --black:#0d0d0d;
    --page:#e7e7ea;
  }
  *{box-sizing:border-box;margin:0;padding:0}
  html,body{width:1041px;height:1200px;overflow:hidden;background:var(--page)}
  body{font-family:"Open Sans",sans-serif;color:var(--ink)}
  .flier{position:absolute;left:97px;top:0;width:846px;height:1200px;overflow:hidden;background:var(--white)}
  .flier-art{position:absolute;inset:0}
  .brand-badge{position:absolute;left:567px;top:307px;width:228px;height:228px;border-radius:50%;
    background:var(--white);border:5px solid var(--blue);display:flex;align-items:center;justify-content:center}
  .brand-name{font-weight:700;font-size:22px;color:var(--blue);text-align:center;line-height:1.2}
  .headline{position:absolute;left:150px;top:540px;font-weight:800;font-size:100px;line-height:1;letter-spacing:-1px;white-space:nowrap}
  .headline .go{color:var(--green)}
  .headline .solar{color:var(--blue)}
  .tagline{position:absolute;left:150px;top:640px;width:510px;text-align:center;font-weight:700;font-size:19px;color:var(--orange-dark);letter-spacing:.2px;white-space:nowrap}
  .easy-card{position:absolute;left:59px;top:681px;width:343px;height:364px;background:rgba(255,255,255,.95);border-radius:8px;overflow:hidden;box-shadow:0 2px 6px rgba(0,0,0,.2)}
  .easy-title{height:69px;background:linear-gradient(var(--orange),var(--orange-dark));color:var(--white);font-weight:800;font-size:33px;display:flex;align-items:center;justify-content:center}
  .benefits{list-style:none;padding:18px 14px 0 20px}
  .benefits li{position:relative;padding-left:14px;font-size:14px;line-height:16px;margin-bottom:8px}
  .benefits li::before{content:"";position:absolute;left:0;top:4px;border-left:6px solid var(--orange);border-top:4px solid transparent;border-bottom:4px solid transparent}
  .benefits em{font-weight:700}
  .how{padding:18px 14px 0 34px;font-size:13.5px;line-height:19.5px}
  .how h3{font-size:14px;font-weight:700}
  .how b{font-weight:700}
  .rebate{position:absolute;left:475px;top:690px;width:304px;height:304px;border-radius:50%;
    background:radial-gradient(circle at 50% 35%,#e6f4c9 0%,var(--green-light) 35%,var(--green) 75%);
    text-align:center;font-family:"Arimo",sans-serif}
  .rebate-lead{margin-top:48px;font-size:31px;line-height:36px;color:var(--ink)}
  .rebate-amount{font-family:"Open Sans",sans-serif;font-weight:800;font-size:74px;line-height:84px;color:var(--orange)}
  .rebate-label{font-family:"Open Sans",sans-serif;font-weight:800;font-size:33px;color:var(--white)}
  .installer{position:absolute;left:493px;top:1003px;width:269px;height:64px;border-radius:8px;background:linear-gradient(var(--orange),var(--orange-dark));color:var(--white);text-align:center;font-weight:600;font-size:20px;line-height:29px;padding-top:3px}
  .disclaimer{position:absolute;left:0;top:1080px;width:846px;height:36px;background:var(--black);color:var(--white);font-size:12.5px;display:flex;align-items:center;justify-content:center}
  .footer-text{position:absolute;color:var(--white)}
  .address{left:36px;top:1133px;font-weight:700;font-size:15px;line-height:23px;display:flex;gap:10px}
  .web{left:312px;top:1147px;font-weight:700;font-size:15px;display:flex;gap:8px;align-items:center}
  .call{left:622px;top:1130px;font-size:27px;line-height:32px}
  .call strong{display:block;font-weight:700;font-size:28px}
  .icon{flex:none}
</style>
</head>
<body>
<main class="flier">
  <svg class="flier-art" viewBox="0 0 846 1200" width="846" height="1200">
    <defs>
      <linearGradient id="panelSky" x1="0" y1="0" x2="1" y2="1">
        <stop offset="0" stop-color="#d6e8f6"/>
        <stop offset=".45" stop-color="#8fbde6"/>
        <stop offset="1" stop-color="#2a5fa8"/>
      </linearGradient>
      <radialGradient id="cloud" cx=".5" cy=".5" r=".5">
        <stop offset="0" stop-color="#ffffff" stop-opacity=".95"/>
        <stop offset=".6" stop-color="#f2f7fc" stop-opacity=".8"/>
        <stop offset="1" stop-color="#e6f0fa" stop-opacity="0"/>
      </radialGradient>
      <linearGradient id="landscape" x1="0" y1="0" x2="0" y2="1">
        <stop offset="0" stop-color="#a9c8e6"/>
        <stop offset=".18" stop-color="#6d8f78"/>
        <stop offset=".38" stop-color="#3f6b3a"/>
        <stop offset=".62" stop-color="#3a5f95"/>
        <stop offset="1" stop-color="#6f8a4a"/>
      </linearGradient>
    </defs>
    <g role="img" aria-label="Rows of solar panels under a bright blue sky with clouds">
      <rect width="846" height="1080" fill="url(#panelSky)"/>
      <ellipse cx="400" cy="640" rx="420" ry="120" fill="url(#cloud)"/>
    </g>
    <path d="M0 330 C120 450 300 540 520 555 C650 560 760 480 846 380 V330 C760 430 650 510 520 505 C320 495 130 420 0 300 Z" fill="var(--green)"/>
    <path d="M0 300 C130 420 320 500 520 505 C650 505 760 420 846 330 V290 C760 380 640 470 520 470 C320 465 130 380 0 260 Z" fill="var(--blue)"/>
    <path d="M0 0 H846 V290 C760 380 640 470 520 470 C320 465 130 380 0 260 Z" fill="url(#landscape)" role="img" aria-label="House with a solar panel roof in green countryside"/>
    <polygon points="0,1116 300,1116 272,1200 0,1200" fill="var(--orange)"/>
    <polygon points="300,1116 603,1116 575,1200 272,1200" fill="var(--green)"/>
    <polygon points="609,1116 846,1116 846,1200 581,1200" fill="var(--blue)"/>
    <polygon points="300,1116 309,1116 281,1200 272,1200" fill="var(--white)"/>
    <polygon points="603,1116 609,1116 581,1200 575,1200" fill="var(--white)"/>
  </svg>

  <div class="brand-badge"><span class="brand-name">Brightfield<br>Energy</span></div>

  <h1 class="headline"><span class="go">GO</span> <span class="solar">SOLAR</span></h1>
  <p class="tagline">GET GRANDFATHERED BEFORE THE NEW RATE DEADLINE</p>

  <section class="easy-card">
    <h2 class="easy-title">WE MAKE IT EASY</h2>
    <ul class="benefits">
      <li><em>$0 Down,</em> no upfront cost</li>
      <li><em>save up to 90%</em> off your utility bill</li>
      <li>Protect againt inflation &amp; energy costs increases from your utility company</li>
      <li>Provide clean, relible energy for your family <em>prowered by the sun.</em></li>
    </ul>
    <div class="how">
      <h3>How it works...</h3>
      <p>your solar system allows you to <b>generate <i>your own clean power</i></b> and COSTS LESS than your current utility company. simply pay by the month, like you do now...but at a LOWER rate and <b><i>START SAVING IMMEDIATELY.</i></b></p>
    </div>
  </section>

  <section class="rebate">
    <p class="rebate-lead">Call Today<br>and Receive a</p>
    <p class="rebate-amount">$500</p>
    <p class="rebate-label">CASH REBATE</p>
  </section>

  <p class="installer">Harlow Electric<br>ROC#417520/209386</p>

  <p class="disclaimer">Limited time offer.Admust be present at time of purchase. Callfor details. Not valid with anyother offer or on previous purchases.</p>

  <p class="footer-text address">
    <svg class="icon" width="18" height="18" viewBox="0 0 18 18"><circle cx="9" cy="9" r="8" fill="none" stroke="#fff" stroke-width="1.3"/><path d="M9 4a3 3 0 0 0-3 3c0 2.3 3 6 3 6s3-3.7 3-6a3 3 0 0 0-3-3z" fill="#fff"/><circle cx="9" cy="7" r="1" fill="var(--orange)"/></svg>
    <span>4815 W Linden Rd A- 220<br>Mesa AZ 85201</span>
  </p>
  <p class="footer-text web">
    <svg class="icon" width="16" height="16" viewBox="0 0 16 16" fill="none" stroke="#fff" stroke-width="1.2"><circle cx="8" cy="8" r="7"/><ellipse cx="8" cy="8" rx="3" ry="7"/><path d="M1 8h14M2.5 4.5h11M2.5 11.5h11"/></svg>
    <span>www.brightfieldsolar.com</span>
  </p>
  <p class="footer-text call">Call Us<strong>602-555-0148</strong></p>
</main>
</body>
</html>
```